Weight gainer supplement design

Looking for a design for a weight gainer /meal replacement supplement. The black plastic tub we will use has 2 spaces for sticker one around the rim approx 2.8cm tall x 30cm wideAnother around the main tub. The main sticker size will be 18cm tall by 70cm this will include the front of the product then wrap around to show the nutritional table.The brand is KRV (Kestrel vigor works) and the product will be called ALPHA MASSThe target ordience is men aged 16-35 its should have a profesional feel to it. The product comes in a black tub, the colores we would like to use are black and blue or red or gold or silver but we are open to suggestions and would like artistic imput. Are logo for KRV is attached but can be changed if the designer prefers.Attached is 1. KRV logo2. Image of similar product that comes in the same tub3 - 5 - images of similar products that we like the design of.The product is 12lbs and will be vanilla flavor. Please ask for more suggestions if needed, I have kept this description short to try and get artistic input.Thanks in advance :)

Target Market(s)

18-35 males who go to the gym

Industry/Entity Type

Fitness

Colors

Designer to choose colors to be used in the design.

Requirements
Must have
• name titan bulk, logo KRV
Should not have
• images of people

```html
<!DOCTYPE html>
<html lang="en">
<head>
<meta charset="utf-8">
<title>TITAN BULK – Label Set</title>
<link href="https://fonts.googleapis.com/css2?family=Krona+One&family=Orbitron:wght@700;900&family=Arimo:wght@400;700&display=swap" rel="stylesheet">
<style>
  :root{
    --page:#ececec;
    --black:#0b0b0b;
    --red:#d3141c;
    --red-dark:#7a0a0e;
    --red-bright:#ff2a2a;
    --white:#ffffff;
  }
  *{box-sizing:border-box;margin:0;padding:0}
  html,body{width:1200px;height:900px;overflow:hidden;background:var(--page)}
  body{position:relative;font-family:"Arimo",Arial,sans-serif}

  .rim-label{
    position:absolute;left:40px;top:170px;width:1120px;height:96px;
    background:linear-gradient(180deg,var(--red-bright) 0%,var(--red) 45%,var(--red-dark) 100%);
    display:flex;align-items:center;justify-content:center;
    box-shadow:0 6px 14px rgba(0,0,0,.18);
  }
  .rim-label__text{
    font-family:"Orbitron",sans-serif;font-weight:900;color:var(--white);font-size:44px;
    letter-spacing:3px;white-space:nowrap;
  }

  .main-label{
    position:absolute;left:40px;top:330px;width:1120px;height:288px;
    background:var(--black);overflow:hidden;box-shadow:0 8px 18px rgba(0,0,0,.22);
  }
  .main-label__art{position:absolute;inset:0}

  .front{position:absolute;left:400px;top:0;width:320px;height:288px;text-align:center;color:var(--white)}
  .brand{position:absolute;left:0;right:0;top:20px;display:flex;justify-content:center;align-items:center;gap:10px}
  .brand__mark{width:18px;height:18px;border-radius:50%;background:var(--white)}
  .brand__name{font-family:"Krona One",sans-serif;font-size:32px;letter-spacing:2px;color:var(--white);line-height:1}
  .product-name{position:absolute;left:0;right:0;font-family:"Krona One",sans-serif;color:var(--white);line-height:1;white-space:nowrap}
  .product-name--top{top:84px;font-size:48px;letter-spacing:1px}
  .product-name--bottom{top:136px;font-size:54px;letter-spacing:1px}
  .subtitle{position:absolute;left:0;right:0;top:198px;font-family:"Orbitron",sans-serif;font-weight:700;font-size:12px;letter-spacing:1px;white-space:nowrap}
  .flavor{position:absolute;left:50%;transform:translateX(-50%);top:215px;background:var(--black);border-radius:12px;padding:3px 24px;font-family:"Orbitron",sans-serif;font-weight:700;font-size:13px;white-space:nowrap}
  .net-weight{position:absolute;left:14px;top:244px;text-align:left;font-family:"Orbitron",sans-serif;font-weight:700;line-height:1}
  .net-weight__label{font-size:11px}
  .net-weight__value{font-family:"Krona One",sans-serif;font-size:15px;margin-top:3px}
  .benefits{position:absolute;left:100px;top:240px;display:flex;gap:8px;list-style:none}
  .benefit{width:36px;text-align:center}
  .benefit__icon{width:34px;height:34px;border-radius:50%;border:2px solid var(--white);background:var(--black);display:block;margin:0 auto}
  .benefit__icon--figure{background:radial-gradient(circle at 50% 45%,#3a3a3a 0%,#111 75%)}
  .benefit__label{font-size:4.5px;font-weight:700;letter-spacing:.2px;margin-top:2px;display:block}
  .calories{position:absolute;left:232px;top:244px;text-align:left;line-height:1}
  .calories__value{font-family:"Krona One",sans-serif;font-size:22px}
  .calories__label{font-family:"Orbitron",sans-serif;font-weight:700;font-size:6px;margin-top:3px}

  .nutrition{
    position:absolute;left:852px;top:18px;width:212px;background:var(--white);color:var(--black);
    border:1px solid var(--black);padding:3px 4px;font-size:4.4px;line-height:1.3;
  }
  .nutrition__title{font-weight:700;font-size:11px;line-height:1}
  .nutrition__rule{border-top:3px solid var(--black);margin:2px 0}
  .nutrition__rule--thin{border-top-width:1px}
  .nutrition__cols{display:grid;grid-template-columns:1fr 1fr;column-gap:6px}
  .nutrition__row{display:flex;justify-content:space-between}
  .nutrition__grid{display:grid;grid-template-columns:repeat(3,1fr);column-gap:4px}
  .nutrition__grid--limits{grid-template-columns:1.4fr 1fr 1fr 1fr}
  .nutrition b{font-weight:700}

  .disclaimer{position:absolute;left:852px;top:250px;width:225px;color:var(--white);font-size:6.4px;line-height:1.4}
</style>
</head>
<body>

<section class="rim-label" aria-label="Rim label">
  <p class="rim-label__text">STRENGTH | ENERGY | FOCUSE</p>
</section>

<section class="main-label" aria-label="Main wrap label">
  <svg class="main-label__art" width="1120" height="288" viewBox="0 0 1120 288">
    <defs>
      <linearGradient id="redBand" x1="0" y1="0" x2="0" y2="1">
        <stop offset="0" stop-color="#e01b22"/>
        <stop offset="1" stop-color="#8a0c10"/>
      </linearGradient>
    </defs>
    <rect x="0" y="0" width="1120" height="288" fill="#121212" role="img" aria-label="Dark perforated metal texture"/>
    <path d="M0 200 C 300 190, 420 170, 560 172 C 760 175, 900 150, 1120 120 L1120 288 L0 288 Z" fill="url(#redBand)" role="img" aria-label="Red scratched texture band"/>
    <path d="M470 0 A 120 78 0 0 0 650 0" fill="none" stroke="#c7161d" stroke-width="4"/>
  </svg>

  <div class="front">
    <div class="brand"><span class="brand__mark"></span><span class="brand__name">KRV</span></div>
    <h1 class="product-name product-name--top">TITAN</h1>
    <p class="product-name product-name--bottom">BULK</p>
    <p class="subtitle">MASS GAINER MUSLE POWDER</p>
    <p class="flavor">VANILLA FLAVOR</p>
    <div class="net-weight"><p class="net-weight__label">NET WT</p><p class="net-weight__value">12LBS</p></div>
    <ul class="benefits">
      <li class="benefit"><span class="benefit__icon benefit__icon--figure" role="img" aria-label="Bodybuilder silhouette icon"></span><span class="benefit__label">BODYBUILDING</span></li>
      <li class="benefit">
        <svg class="benefit__icon" viewBox="0 0 34 34" aria-hidden="true"><path d="M8 22 A10 10 0 0 1 26 22" fill="none" stroke="#fff" stroke-width="2"/><line x1="17" y1="22" x2="22" y2="14" stroke="#fff" stroke-width="2"/></svg>
        <span class="benefit__label">PERFORMANCE</span></li>
      <li class="benefit">
        <svg class="benefit__icon" viewBox="0 0 34 34" aria-hidden="true"><ellipse cx="17" cy="17" rx="11" ry="4" fill="none" stroke="#fff" stroke-width="1.5"/><ellipse cx="17" cy="17" rx="4" ry="11" fill="none" stroke="#fff" stroke-width="1.5"/><circle cx="17" cy="17" r="2" fill="#fff"/></svg>
        <span class="benefit__label">ENERGY</span></li>
    </ul>
    <div class="calories"><p class="calories__value">800</p><p class="calories__label">HIGH CALORIES</p></div>
  </div>

  <div class="nutrition">
    <p class="nutrition__title">Nutrition Facts</p>
    <p>Serving Size 433g (3 cups)</p>
    <p>Servings Per Container 10</p>
    <div class="nutrition__rule"></div>
    <p><b>Amount Per Serving</b></p>
    <p>Calories 1677</p>
    <div class="nutrition__rule"></div>
    <div class="nutrition__cols">
      <div>
        <div class="nutrition__row"><b>% Daily Value*</b></div>
        <div class="nutrition__row"><span><b>Total Fat</b> 17g</span><span>26%</span></div>
        <div class="nutrition__row"><span>&nbsp; Saturated Fat 5g</span><span>24%</span></div>
        <div class="nutrition__row"><span>&nbsp; Trans Fat 0g</span><span></span></div>
        <div class="nutrition__row"><span><b>Cholesterol</b> 168mg</span><span>56%</span></div>
        <div class="nutrition__row"><span><b>Sodium</b> 934mg</span><span>39%</span></div>
      </div>
      <div>
        <div class="nutrition__row"><b>% Daily Value*</b></div>
        <div class="nutrition__row"><span><b>Potassium</b> 758mg</span><span>22%</span></div>
        <div class="nutrition__row"><span><b>Total Carbohydrate</b> 291g</span><span>97%</span></div>
        <div class="nutrition__row"><span>&nbsp; Dietary Fiber 3g</span><span>12%</span></div>
        <div class="nutrition__row"><span>&nbsp; Sugars 22g</span><span></span></div>
        <div class="nutrition__row"><span><b>Protein</b> 90g</span><span>180%</span></div>
      </div>
    </div>
    <div class="nutrition__rule"></div>
    <div class="nutrition__grid">
      <span>Vitamin A 144%</span><span>Vitamin C 143%</span><span>Calcium 86%</span>
      <span>Iron 15%</span><span>Vitamin D 143%</span><span>Vitamin E 157%</span>
      <span>Vitamin K 143%</span><span>Thiamin 144%</span><span>Riboflavin 203%</span>
      <span>Niacin 144%</span><span>Vitamin B6 145%</span><span>Folate 140%</span>
      <span>Vitamin B12 143%</span><span>Biotin 143%</span><span>Pantothenic Acid 143%</span>
      <span>Phosphorous 42%</span><span>Magnesium 27%</span><span>Zinc 2%</span>
      <span>Selenium 19%</span><span>Copper 29%</span><span>Manganese 14%</span>
      <span>Chromium 1%</span><span>Molybdenum 2%</span><span>Chloride 20%</span>
    </div>
    <div class="nutrition__rule nutrition__rule--thin"></div>
    <p>*Percent Daily Values are based on a 2,000 calorie diet. Your daily values may be higher or lower depending on your caloric needs.</p>
    <div class="nutrition__grid nutrition__grid--limits">
      <span></span><span>Calories:</span><span>2,000</span><span>2,500</span>
      <span>Total Fat</span><span>Less than</span><span>65g</span><span>80g</span>
      <span>Sat. Fat</span><span>Less than</span><span>20g</span><span>25g</span>
      <span>Cholesterol</span><span>Less than</span><span>300mg</span><span>300mg</span>
      <span>Sodium</span><span>Less than</span><span>2,400mg</span><span>2,400mg</span>
      <span>Total Carbohydrate</span><span></span><span>300g</span><span>375g</span>
      <span>Dietary Fiber</span><span></span><span>25g</span><span>30g</span>
    </div>
    <div class="nutrition__rule nutrition__rule--thin"></div>
    <p>Calories per gram: &nbsp; Fat 9 &nbsp;•&nbsp; Carbohydrate 4 &nbsp;•&nbsp; Protein 4</p>
  </div>

  <p class="disclaimer">This product is not intended to diagnose, treat, cure or prevent any disease. These statements have not been evaluated by the Food &amp; Drug Administration.</p>
</section>

</body>
</html>
```